Business Card - Brisk Works
Stout Harbor BC
Project: Business Card - Brisk Works
Business Card - Brisk Works - Manufacturing
Creative Brief
Professional
Gordon Pratchett
gpratchett@stoutharbor-mail.com
"Build and Thrive"
emagineitgroup emagineitgroup
I accidentally erased #67, can it be put back on?
I like #105 as a start with the following changes: 1. the bottom portion of the card is black I would like this to be eliminated and center (2) shiny gold lines centered and measuring : TOP LINE - 2 6/8" AND THE BOTTOM LINE = 1 5/8" . These two lines should be centered . THE DISTANCE APART SHOULD BE 1/16". I would like for the two 'shiny gold lines' to be centered between the logo on top and my information below. I would also like for my name: GORDON PRATCHETT to be in bold black and all caps. I would like to see the rest of the info not in bold, but in black font. I would like the pareto chart (3) to the right on top of the black line to be completely eliminated. I only want to have a card that is one sided. I would also like to see the card as it is, currently, with the font in the black section on the lower half of the card, in white font.
Im liking the clear cards as well. Please give me more options on clear business cards that are perhaps not as generic.
glassfairy glassfairy
plz upload the logo file too
I have a current Business Card i would like to Add for an example. Please let me know where to add it.

```html
<!DOCTYPE html>
<html lang="en">
<head>
<meta charset="utf-8">
<title>Business Card – Stout Harbor</title>
<link href="https://fonts.googleapis.com/css2?family=Open+Sans:wght@400;600;700&display=swap" rel="stylesheet">
<style>
  :root {
    --backdrop: #8e8e8e;
    --card: #ffffff;
    --ink: #1e1e1e;
    --ink-soft: #3a3a3a;
    --gold-light: #e6cf8f;
    --gold: #c9a455;
    --gold-dark: #a9833a;
    --band: #1c1c1c;
    --band-text: #ffffff;
  }
  * { box-sizing: border-box; margin: 0; padding: 0; }
  html, body { width: 1200px; height: 878px; overflow: hidden; }
  body {
    background: var(--backdrop);
    font-family: "Open Sans", Arial, sans-serif;
    color: var(--ink);
    position: relative;
  }
  .card {
    position: absolute;
    left: 100px;
    top: 153px;
    width: 1000px;
    height: 572px;
    background: var(--card);
    box-shadow: 0 14px 32px rgba(0,0,0,.28);
    overflow: hidden;
  }
  .card-graphics { position: absolute; inset: 0; }
  .brand {
    position: absolute;
    left: 90px;
    top: 120px;
    display: flex;
    align-items: center;
    gap: 16px;
  }
  .brand-mark {
    width: 20px; height: 20px;
    background: var(--gold);
  }
  .brand-name {
    font-size: 42px;
    font-weight: 700;
    letter-spacing: 1px;
    color: var(--ink);
    text-transform: uppercase;
  }
  .brand-tagline {
    position: absolute;
    left: 126px;
    top: 180px;
    font-size: 20px;
    letter-spacing: 4px;
    color: var(--ink-soft);
    text-transform: uppercase;
  }
  .person {
    position: absolute;
    left: 590px;
    top: 205px;
  }
  .person-name { font-size: 30px; font-weight: 700; color: var(--ink); }
  .person-title { font-size: 18px; color: var(--ink-soft); margin-top: 2px; }
  .address { margin-top: 22px; font-size: 18px; line-height: 1.35; color: var(--ink-soft); }
  .contact-list {
    list-style: none;
    position: absolute;
    left: 600px;
    top: 355px;
    font-size: 18px;
    color: var(--ink-soft);
  }
  .contact-list li { display: flex; align-items: center; gap: 12px; height: 28px; }
  .contact-list svg { width: 16px; height: 16px; fill: var(--ink); }
  .website {
    position: absolute;
    right: 60px;
    bottom: 16px;
    font-size: 19px;
    letter-spacing: 1px;
    color: var(--band-text);
  }
</style>
</head>
<body>
  <div class="card">
    <svg class="card-graphics" viewBox="0 0 1000 572" width="1000" height="572" aria-hidden="true">
      <defs>
        <linearGradient id="goldSheen" x1="0" y1="0" x2="1" y2="0">
          <stop offset="0" stop-color="var(--gold-dark)"/>
          <stop offset="0.5" stop-color="var(--gold-light)"/>
          <stop offset="1" stop-color="var(--gold)"/>
        </linearGradient>
      </defs>
      <polygon points="0,388 365,498 365,518 0,420" fill="url(#goldSheen)"/>
      <polygon points="330,506 1000,506 1000,572 410,572" fill="var(--band)"/>
      <polygon points="0,420 365,518 410,572 0,572" fill="var(--card)"/>
    </svg>

    <div class="brand">
      <span class="brand-mark"></span>
      <span class="brand-name">Stout Harbor, Inc.</span>
    </div>
    <div class="brand-tagline">Build and Thrive</div>

    <div class="person">
      <div class="person-name">Gordon Pratchett</div>
      <div class="person-title">Managing Director</div>
      <div class="address">P.O Box 88 Quay Lane<br>Harbor City Region 512</div>
    </div>

    <ul class="contact-list">
      <li>
        <svg viewBox="0 0 16 16"><path d="M3 1l3 3-2 2c1 2 3 4 5 5l2-2 3 3-2 3C6 15 1 10 1 3z"/></svg>
        <span>555 014 2290</span>
      </li>
      <li>
        <svg viewBox="0 0 16 16"><path d="M2 5h12v9H2zM4 1h8v3H4z"/></svg>
        <span>555 014 2291</span>
      </li>
      <li>
        <svg viewBox="0 0 16 16"><path d="M4 0h8v16H4zM6 2v10h4V2z"/></svg>
        <span>555 014 2292</span>
      </li>
      <li>
        <svg viewBox="0 0 16 16"><path d="M1 3h14v10H1zM2 4l6 5 6-5v-0z" /></svg>
        <span>gpratchett@stoutharbor-mail.com</span>
      </li>
    </ul>

    <div class="website">stoutharbor-works.com</div>
  </div>
</body>
</html>
```